BrightQuill PowerPoint Design

We need a very cool power-point template done for BrightQuill. We need it to drive the message of technology, speed and innovation. This is for a racing proposal to for our indy car team. I will attach our logo.

Target Market(s)

This presentation is for our INDY RACE CAR TEAM OVERVIEW... The Theme is: Speed, Technology and Innovation

Industry/Entity Type

Racing

Colors

Designer to choose colors to be used in the design.

Requirements
Must have
• Intro Slide with Logo - Must look very cool
Template Slide for Content
Ending Slide with something like "Thanks BrightQuill!"
Nice to have
• Please see the example ppt deck from Lomerix a previous company to see the slide template... Also see a old template for BrightQuill

```html
<!DOCTYPE html>
<html lang="en">
<head>
<meta charset="utf-8">
<title>BrightQuill Presentation Template</title>
<link rel="stylesheet" href="https://fonts.googleapis.com/css2?family=Open+Sans:wght@400;700&family=Ubuntu:wght@400&family=Oswald:wght@700&family=Arimo:wght@400&family=Allura&display=swap">
<style>
:root{
  --stage-dark:#333436;
  --stage-mid:#5b5c5e;
  --blue:#2a80c4;
  --orange:#e8a020;
  --grey-text:#8a8a8a;
  --dark-text:#222;
  --white:#fff;
}
*{margin:0;padding:0;box-sizing:border-box}
html,body{width:1200px;height:999px;overflow:hidden}
body{
  position:relative;
  background:radial-gradient(ellipse at 50% 45%,var(--stage-mid) 0%,var(--stage-dark) 85%);
  font-family:"Open Sans",Arial,sans-serif;
}
.slide{position:absolute;width:535px;height:401px;overflow:hidden;background:var(--white);box-shadow:0 2px 6px rgba(0,0,0,.35)}
.slide--intro{left:65px;top:103px}
.slide--content{left:617px;top:103px}
.slide--text{left:67px;top:543px}
.slide--closing{left:617px;top:541px}
.slide__bg{position:absolute;inset:0;width:100%;height:100%}
.slide__inner{position:absolute;inset:0}

.brand{position:absolute;left:0;right:0;text-align:center}
.brand__name{font-family:"Ubuntu",sans-serif;font-weight:400;font-size:52px;color:var(--blue);line-height:1}
.brand__tagline{margin-top:6px;font-family:"Ubuntu",sans-serif;font-size:15px;color:var(--blue)}
.brand--closing .brand__name{font-size:43px}
.brand--closing .brand__tagline{font-size:13px;margin-top:4px}

.slide__title-main{position:absolute;left:0;right:0;top:194px;text-align:center;font-weight:700;font-size:38px;color:var(--white);letter-spacing:.5px}
.slide__url{position:absolute;left:0;right:0;top:348px;text-align:center;font-weight:700;font-size:21px;color:var(--blue)}

.thanks{position:absolute;left:0;right:0;top:22px;text-align:center;font-family:"Allura",cursive;font-size:96px;color:var(--white);line-height:1}

.heading{position:absolute;left:41px;font-family:"Oswald",sans-serif;font-weight:700;font-size:38px;color:var(--orange);letter-spacing:3.3px;line-height:1}
.subheading{position:absolute;left:44px;top:99px;font-family:"Arimo",sans-serif;font-size:19px;color:#444}
.lead{position:absolute;left:46px;top:146px;font-family:"Arimo",sans-serif;font-size:29px;line-height:35px;color:var(--grey-text);letter-spacing:-.4px}
.point{position:absolute;left:48px;top:244px;display:flex;gap:18px}
.point__icon{width:40px;height:40px;margin-top:10px}
.point__title{font-family:"Arimo",sans-serif;font-size:17.5px;color:#111}
.point__body{font-family:"Arimo",sans-serif;font-size:12px;line-height:16px;color:var(--grey-text);width:240px}

.body-copy{position:absolute;left:18px;width:471px;top:118px;font-family:"Arimo",Arial,sans-serif;font-size:11.4px;line-height:13.4px;color:var(--dark-text);text-align:justify}
.body-copy p+p{margin-top:13px}

.footer-url{position:absolute;right:66px;bottom:15px;font-weight:700;font-size:10px;color:#111}
</style>
</head>
<body>

<section class="slide slide--intro">
  <svg class="slide__bg" viewBox="0 0 535 401" preserveAspectRatio="none" aria-hidden="true">
    <defs>
      <linearGradient id="introNavy" x1="0" y1="0" x2="1" y2="1">
        <stop offset="0" stop-color="#0c3a63"/><stop offset=".6" stop-color="#08294a"/><stop offset="1" stop-color="#06213c"/>
      </linearGradient>
      <linearGradient id="introSweep" x1="0" y1="0" x2="1" y2="0">
        <stop offset="0" stop-color="#1d5fa8"/><stop offset=".5" stop-color="#2a86d4"/><stop offset="1" stop-color="#283a8e"/>
      </linearGradient>
    </defs>
    <path d="M0 0H535V270C420 320 300 340 180 318C110 305 50 285 0 270Z" fill="url(#introNavy)"/>
    <path d="M0 40C120 10 260 70 535 20" stroke="#1a5a92" stroke-opacity=".35" stroke-width="40" fill="none"/>
    <path d="M0 270C80 300 200 335 320 330C420 325 490 300 535 272V282C480 318 400 340 300 342C190 344 90 310 0 285Z" fill="url(#introSweep)"/>
    <path d="M0 285C90 312 200 342 300 344C400 344 480 320 535 284" stroke="#000" stroke-width="3" fill="none"/>
  </svg>
  <div class="slide__inner">
    <div class="brand" style="top:98px">
      <div class="brand__name">BrightQuill</div>
      <div class="brand__tagline">Built for Speed, Driven by Bold New Innovation</div>
    </div>
    <div class="slide__title-main">PRESENTATION</div>
    <div class="slide__url">www.brightquill.com</div>
  </div>
</section>

<section class="slide slide--content">
  <svg class="slide__bg" viewBox="0 0 535 401" preserveAspectRatio="none" aria-hidden="true">
    <defs>
      <linearGradient id="bandA" x1="0" y1="0" x2="1" y2="0">
        <stop offset="0" stop-color="#2b2f7a"/><stop offset=".5" stop-color="#2a90da"/><stop offset="1" stop-color="#2b2f7a"/>
      </linearGradient>
    </defs>
    <path d="M0 120C150 20 350 10 535 80" stroke="#d9dbe8" stroke-width="30" fill="none" opacity=".6"/>
    <path d="M380 0C460 80 520 200 500 320" stroke="#dcdde8" stroke-width="2" fill="none"/>
    <path d="M420 0C500 90 540 210 520 330" stroke="#e3e4ee" stroke-width="14" fill="none" opacity=".6"/>
    <path d="M0 381H280C288 381 288 391 296 391H535V401H0Z" fill="url(#bandA)"/>
  </svg>
  <div class="slide__inner">
    <div class="heading" style="top:56px">LOREM IPSUM</div>
    <div class="subheading">Consectetuer adipiscing elit.</div>
    <div class="lead">Lorem ipsum dolor sit amet,<br>consectetuer adipiscing elit.</div>
    <div class="point">
      <svg class="point__icon" viewBox="0 0 40 40" aria-hidden="true">
        <path d="M6 34L30 10M14 8H32V26" stroke="var(--orange)" stroke-width="7" fill="none" stroke-linecap="round" stroke-linejoin="round"/>
      </svg>
      <div>
        <div class="point__title">Lorem ipsum dolor sit amet.</div>
        <div class="point__body">Lorem ipsum dolor sit amet, consectetuer elit. Duis pulvinar lectus. Fusce lacinia. Cra tortor, dignissim eu, sollicitudin eu, conseq</div>
      </div>
    </div>
    <div class="footer-url">www.brightquill.com</div>
  </div>
</section>

<section class="slide slide--text">
  <svg class="slide__bg" viewBox="0 0 535 401" preserveAspectRatio="none" aria-hidden="true">
    <defs>
      <linearGradient id="bandB" x1="0" y1="0" x2="1" y2="0">
        <stop offset="0" stop-color="#2b2f7a"/><stop offset=".5" stop-color="#2a90da"/><stop offset="1" stop-color="#2b2f7a"/>
      </linearGradient>
    </defs>
    <path d="M0 110C150 20 350 10 535 70" stroke="#d9dbe8" stroke-width="30" fill="none" opacity=".6"/>
    <path d="M390 0C460 70 520 180 510 300" stroke="#dcdde8" stroke-width="2" fill="none"/>
    <path d="M0 381H280C288 381 288 391 296 391H535V401H0Z" fill="url(#bandB)"/>
  </svg>
  <div class="slide__inner">
    <div class="heading" style="top:54px;left:17px">LOREM IPSUM</div>
    <div class="body-copy">
      <p>Lorem Ipsum is simply dummy text of the printing and typesetting industry. Lorem Ipsum has been the industry's standard dummy text ever since the 1500s, when an unknown printer took a galley of type and scrambled it to make a type specimen book. It has survived not only five centuries, but also the leap into electronic typesetting, remaining essentially unchanged. It was popularised in the 1960s with the release of transfer sheets containing Lorem Ipsum passages, and more recently with desktop publishing software and modern layout tools including versions of Lorem Ipsum.</p>
      <p>Lorem Ipsum is simply dummy text of the printing and typesetting industry. Lorem Ipsum has been the industry's standard dummy text ever since the 1500s, when an unknown printer took a galley of type and scrambled it to make a type specimen book. It has survived not only five centuries, but also the leap into electronic typesetting, remaining essentially unchanged. It was popularised in the 1960s with the release of transfer sheets containing Lorem Ipsum passages, and more recently with desktop publishing software and modern layout tools including versions of Lorem Ipsum.</p>
    </div>
    <div class="footer-url">www.brightquill.com</div>
  </div>
</section>

<section class="slide slide--closing">
  <svg class="slide__bg" viewBox="0 0 535 401" preserveAspectRatio="none" aria-hidden="true">
    <defs>
      <linearGradient id="closeNavy" x1="0" y1="0" x2="1" y2="1">
        <stop offset="0" stop-color="#0c3a63"/><stop offset=".6" stop-color="#08294a"/><stop offset="1" stop-color="#06213c"/>
      </linearGradient>
      <linearGradient id="closeSweep" x1="0" y1="0" x2="1" y2="0">
        <stop offset="0" stop-color="#1d5fa8"/><stop offset=".5" stop-color="#2a86d4"/><stop offset="1" stop-color="#283a8e"/>
      </linearGradient>
    </defs>
    <path d="M0 0H535V270C420 320 300 340 180 318C110 305 50 285 0 270Z" fill="url(#closeNavy)"/>
    <path d="M0 40C120 10 260 70 535 20" stroke="#1a5a92" stroke-opacity=".35" stroke-width="40" fill="none"/>
    <path d="M0 270C80 300 200 335 320 330C420 325 490 300 535 272V282C480 318 400 340 300 342C190 344 90 310 0 285Z" fill="url(#closeSweep)"/>
    <path d="M0 285C90 312 200 342 300 344C400 344 480 320 535 284" stroke="#000" stroke-width="3" fill="none"/>
  </svg>
  <div class="slide__inner">
    <div class="thanks">Thanks</div>
    <div class="brand brand--closing" style="top:194px">
      <div class="brand__name">BrightQuill</div>
      <div class="brand__tagline">Built for Speed, Driven by Bold New Innovation</div>
    </div>
    <div class="slide__url">www.brightquill.com</div>
  </div>
</section>

</body>
</html>
```